Spring Style Exclusive Shopping Party for women

We need a postcard design for our Spring Shopping Event. Willow Lane is a women's apparel and accessories store featuring missy, petite and plus sizes. Event is Saturday, April 1 from 9am-10am. Looking for a twist on the spring shopping party idea. Attaching 2 postcards we have previously sent for this event and 2 ideas for what we are looking for in new postcard.

Target Market(s)

women 20+

Industry/Entity Type

Retail

Font styles to use
Serif

Requirements
Must have
• must be eye catching, have the logo, date and time of event,
Nice to have
• woman model

```html
<!DOCTYPE html>
<html lang="en">
<head>
<meta charset="utf-8">
<title>Willow Lane – Spring Shopping Event Postcard</title>
<link rel="stylesheet" href="https://fonts.googleapis.com/css2?family=Gelasio:wght@400;700&family=Chewy&family=Patrick+Hand+SC&family=Caveat:wght@500&family=Open+Sans:ital@1&display=swap">
<style>
  :root {
    --page: #ffffff;
    --teal: #6fbfc0;
    --white: #ffffff;
    --ink: #1b1b1b;
    --red: #c0141b;
    --badge-red: #e8141a;
    --rule: #555555;
    --model-light: #e9ddd4;
    --model-dark: #8fbfbd;
    --floral-a: #f3ecd8;
    --floral-b: #e6e7cf;
    --floral-c: #f1d9bd;
    --floral-d: #dfe6cf;
    --petal: #fdfbf4;
    --petal-core: #f2b233;
  }
  * { box-sizing: border-box; margin: 0; padding: 0; }
  html, body { width: 781px; height: 1200px; overflow: hidden; background: var(--page); }
  .canvas { position: relative; width: 781px; height: 1200px; }

  .card { position: absolute; left: 30px; width: 699px; overflow: hidden; }
  .card--front { top: 30px; height: 546px; background: var(--teal); }
  .card--back { top: 600px; height: 552px; border: 1px solid #d8d8d8; }

  /* front */
  .title {
    position: absolute; left: 55px; top: 58px;
    font-family: "Chewy", cursive; font-size: 112px; line-height: 1;
    color: var(--white); letter-spacing: 2px;
    text-shadow: 3px 4px 0 rgba(0,0,0,0.12);
  }
  .subtitle {
    position: absolute; left: 142px; top: 190px;
    font-family: "Patrick Hand SC", cursive; font-size: 40px; color: var(--white);
    letter-spacing: 1px;
  }
  .flower { position: absolute; border-radius: 50%; background: var(--petal); }
  .flower::after {
    content: ""; position: absolute; left: 35%; top: 35%; width: 30%; height: 30%;
    border-radius: 50%; background: var(--petal-core);
  }
  .flower--top { left: 240px; top: 40px; width: 24px; height: 24px; }
  .flower--side { left: 57px; top: 168px; width: 40px; height: 40px; }
  .butterfly {
    position: absolute; left: 272px; top: 30px; width: 44px; height: 38px;
    background: radial-gradient(circle, #f0b52a, #c27b12); border-radius: 40%;
  }
  .badge {
    position: absolute; left: 58px; top: 247px; width: 126px; height: 126px;
    border-radius: 50%; background: var(--badge-red);
  }
  .badge__tag {
    position: absolute; left: 17px; top: 37px; width: 94px; height: 50px;
    background: var(--white); border-radius: 6px; transform: rotate(-10deg);
    font-family: "Gelasio", serif; font-weight: 700; color: var(--badge-red);
    display: flex; align-items: center; justify-content: center; gap: 2px;
  }
  .badge__num { font-size: 32px; line-height: 1; }
  .badge__off { font-size: 12px; line-height: 1.05; }
  .when {
    position: absolute; left: 205px; color: var(--white);
    font-family: "Caveat", cursive; font-weight: 500;
  }
  .when--date { top: 266px; font-size: 40px; }
  .when--time { top: 324px; font-size: 34px; }
  .brand-name {
    font-family: "Gelasio", serif; font-weight: 700; color: var(--ink);
    white-space: nowrap;
  }
  .front-brand { position: absolute; left: 150px; top: 412px; font-size: 54px; }
  .front-url {
    position: absolute; left: 195px; top: 487px;
    font-family: "Open Sans", sans-serif; font-style: italic; font-size: 16px; color: var(--ink);
  }
  .model {
    position: absolute; left: 498px; top: 10px; width: 184px; height: 525px;
    border-radius: 90px 90px 10px 10px;
    background: linear-gradient(180deg, var(--model-light) 0%, #ead4c4 40%, var(--model-dark) 100%);
    opacity: 0.9;
  }

  /* back */
  .floral {
    position: absolute; inset: 0;
    background:
      radial-gradient(circle at 80% 25%, var(--petal) 0 12%, transparent 30%),
      radial-gradient(circle at 55% 70%, var(--floral-c) 0 10%, transparent 30%),
      radial-gradient(circle at 30% 40%, var(--floral-d) 0 10%, transparent 35%),
      linear-gradient(135deg, var(--floral-a), var(--floral-b));
  }
  .back-brand { position: absolute; left: 84px; top: 48px; font-size: 44px; }
  .back-rule {
    position: absolute; left: 80px; top: 121px; width: 238px; height: 2px; background: var(--rule);
  }
  .back-url {
    position: absolute; left: 80px; top: 128px; width: 238px; text-align: center;
    font-family: "Gelasio", serif; font-weight: 700; font-size: 11px; letter-spacing: 1.6px; color: var(--rule);
  }
  .message {
    position: absolute; left: 31px; top: 156px; width: 370px;
    font-family: "Gelasio", serif; font-size: 17px; line-height: 23px; color: var(--ink);
  }
  .message p { margin-bottom: 10px; }
  .accent { color: var(--red); font-weight: 700; }
  .blank { display: inline-block; width: 72px; border-bottom: 1px solid var(--ink); }
  .store-city { font-weight: 700; }
</style>
</head>
<body>
<main class="canvas">

  <section class="card card--front" aria-label="Postcard front">
    <span class="flower flower--top" role="img" aria-label="Small white daisy"></span>
    <span class="butterfly" role="img" aria-label="Orange butterfly"></span>
    <span class="flower flower--side" role="img" aria-label="White daisy"></span>
    <h1 class="title">SPRING</h1>
    <p class="subtitle">Shopping Event</p>

    <div class="badge">
      <div class="badge__tag"><span class="badge__num">30%</span><span class="badge__off">%<br>OFF</span></div>
    </div>

    <p class="when when--date">Saturday, April 1st</p>
    <p class="when when--time">9am-10am only</p>

    <p class="brand-name front-brand">Willow Lane</p>
    <p class="front-url">www.willowlanedirect.com</p>

    <div class="model" role="img" aria-label="Photo of a woman in a blush dress with a flower crown holding a yellow clutch"></div>
  </section>

  <section class="card card--back" aria-label="Postcard back">
    <div class="floral" role="img" aria-label="Soft photo of spring roses over whitewashed wood planks"></div>

    <p class="brand-name back-brand">Willow Lane</p>
    <span class="back-rule"></span>
    <p class="back-url">www.willowlanedirect.com</p>

    <div class="message">
      <p>Join us for a special early opening only for our favorite <span class="accent">SHOPAHOLICS!</span></p>
      <p>Everyone will receive a gift bag plus special savings opportunities during this event.&nbsp; Pastries and juice will be served to start your day off right!</p>
      <p>Please <span class="accent">RSVP</span> by <span class="blank"></span>. Guests are welcome although reservations are required as seating is limited.</p>
      <p><span class="store-city">LAKEVIEW</span><br>1815 N Maple Grove Road<br>309-555-0186</p>
    </div>
  </section>

</main>
</body>
</html>
```